Vireo Kinetics LLC Sports Therapy and Soft Tissue Injury solutions

We are a company that specializes in Sports Therapy, Physical therapy, muscular rehab, nutrition plans, and personal training. Vireo Kinetics travels around the country and world treating athletes and people in the workforce that have Soft Tissue injuries. We are legally partnered with QMD(Fluent Motion Protocols/fluentmotion.example) in treating endurance athletes ex. SteelWave triathalon. We educate our patients on how to sustain a healthy lifestyle.We need a web design that has a Home page summarizing our services, a Physical therapy page, a Personal training and nutrition page. Our ultimate goal is to build relationships with fitness centers, training facilities, and companies that are implementing preventative health measures for their employees. We want to incorporate the QMD logo and Steelwave logo attached in the website but, we want to use our own name (Vireo Kinetics LLC) as the main draw. We will provide literature for the website.

Target Market(s)

Brisk rig training gyms, Fitness centers, Dance studios, Companies looking for Corporate Wellness programs

Industry/Entity Type

Health And Wellness

Number of Pages Required

4 page

Font styles to use
Sans Serif

Requirements
Must have
• Stock Photos of Athletes training. Examples of Endurance Athletes and Cross training. A mesh of as many sports and training methods as possible. We are a new company and don't have many photos. Easy accessibility to change and add text as the company grows. Fluent Motion protocols logo incorporated in the back ground of the website. Always visible but does not take over the web page
Nice to have
• Sleek and cool, and masculine design. We want the website to stand out without focusing on one individual. We want to use the website to brand the company (Vireo Kinetics LLC) with easy access to social media platforms

```html
<!DOCTYPE html>
<html lang="en">
<head>
<meta charset="utf-8">
<title>Vireo Kinetics – Health And Wellness</title>
<link href="https://fonts.googleapis.com/css2?family=Lato:ital,wght@0,400;0,700;1,400;1,700&family=Montserrat:wght@500;600;700&display=swap" rel="stylesheet">
<style>
:root{
  --green:#6aa22e;
  --blue:#1a6fb5;
  --blue-bar:#1566b3;
  --ink:#222;
  --body:#444;
  --grey-band:#e9e9e9;
  --partner-grey:#8a8a8a;
  --footer:#1b1b1b;
  --footer-text:#d8d8d8;
  --top-rule:#5a5a5a;
}
*{box-sizing:border-box;margin:0;padding:0}
html,body{width:1200px;height:2575px;overflow:hidden;background:#fff}
body{font-family:"Lato",Arial,sans-serif;color:var(--body);position:relative}
.wrap{position:relative;width:1200px;height:2575px;overflow:hidden}

/* header */
.site-header{position:absolute;top:0;left:0;width:1200px;height:112px;background:linear-gradient(#fff,#f3f3f3);border-top:5px solid var(--top-rule)}
.brand{position:absolute;left:100px;top:24px;display:flex;align-items:center;gap:12px}
.brand-dot{width:40px;height:40px;border-radius:50%;background:var(--green)}
.brand-name{font-family:"Montserrat",sans-serif;font-weight:600;font-size:30px;color:var(--green);line-height:1;white-space:nowrap}
.brand-tag{position:absolute;left:152px;top:62px;font-family:"Montserrat",sans-serif;font-weight:600;font-size:15px;color:var(--blue);letter-spacing:1px;white-space:nowrap}
.phone-pill{position:absolute;left:748px;top:16px;width:200px;height:36px;border-radius:18px;background:#e4e4e4;display:flex;align-items:center;white-space:nowrap}
.phone-pill .ico{flex:none;width:36px;height:36px;border-radius:50%;background:var(--green);display:flex;align-items:center;justify-content:center}
.phone-pill span.num{font-family:"Lato",sans-serif;font-weight:700;font-size:16px;color:var(--ink);margin-left:18px}
.social{position:absolute;display:flex;gap:8px}
.social i{display:block;border-radius:50%;background:var(--green)}
.social.top{left:974px;top:16px}
.social.top i{width:37px;height:37px}
.main-nav{position:absolute;left:480px;top:75px;width:622px;display:flex;justify-content:space-between}
.main-nav a{font-family:"Montserrat",sans-serif;font-weight:600;font-size:13px;color:var(--ink);text-decoration:none;text-transform:uppercase;padding:0 0 14px;position:relative;white-space:nowrap}
.main-nav a.active{color:var(--green)}
.main-nav a.active::after{content:"";position:absolute;left:0;right:0;bottom:0;height:4px;background:var(--green)}

/* hero */
.hero{position:absolute;top:112px;left:0;width:1200px;height:478px;overflow:hidden}
.hero-photo{position:absolute;inset:0;
  background:
    linear-gradient(180deg,rgba(255,255,255,.35) 0%,rgba(255,255,255,0) 30%,rgba(0,0,0,0) 70%,rgba(40,50,40,.5) 100%),
    linear-gradient(95deg,#e2e2e2 0%,#b8b8b8 18%,#6f6a66 32%,#8d8f94 44%,#24325a 55%,#1c2950 72%,#2a3a66 88%,#cfd0d4 100%)}
.hero-caption{position:absolute;left:0;bottom:0;width:100%;height:70px;background:rgba(0,0,0,.5);display:flex;align-items:center;justify-content:center}
.hero-caption h2{font-family:"Montserrat",sans-serif;font-weight:700;font-size:28px;color:#fff;white-space:nowrap}
.slide-arrow{position:absolute;top:174px;width:42px;height:42px;background:rgba(30,30,30,.85);display:flex;align-items:center;justify-content:center}
.slide-arrow.prev{left:8px}
.slide-arrow.next{right:8px}

/* headings */
.sec-title{font-family:"Montserrat",sans-serif;font-weight:600;font-size:30px;text-align:center;color:var(--green)}
.sec-title .blue{color:var(--blue)}
.sec-title small{font-size:21px;color:var(--blue)}
.rule{width:82px;height:2px;background:#333;margin:16px auto 0}

/* about */
.about{position:absolute;top:590px;left:0;width:1200px;height:267px;background:#fff}
.about .sec-title{margin-top:38px}
.about p{width:1000px;margin:0 auto;text-align:center;font-size:14px;line-height:21px;color:var(--body)}
.about p.first{margin-top:36px}
.about p+p{margin-top:12px}

/* specialize */
.specialize{position:absolute;top:857px;left:0;width:1200px;height:734px}
.specialize-photo{position:absolute;inset:0;background:linear-gradient(90deg,#d3d8de 0%,#eceef0 35%,#e6e8ea 65%,#d0d5da 100%)}
.specialize .sec-title{position:absolute;top:58px;width:100%}
.specialize .rule{position:absolute;top:112px;left:559px;margin:0}
.spec-lines{position:absolute;left:0;top:0}
.spec-item{position:absolute;left:560px;display:flex;align-items:center}
.spec-ico{width:76px;height:76px;border-radius:50%;background:#fff;display:flex;align-items:center;justify-content:center;box-shadow:0 0 0 1px #ddd}
.spec-ico b{width:64px;height:64px;border-radius:50%;display:flex;align-items:center;justify-content:center}
.spec-ico.green b{background:var(--green)}
.spec-ico.blue b{background:var(--blue)}
.spec-text{margin-left:15px;width:400px}
.spec-text h3{font-family:"Montserrat",sans-serif;font-weight:600;font-size:17px;color:#111;letter-spacing:.5px}
.spec-text p{font-size:12px;line-height:18px;color:#333;margin-top:6px}

/* testimonials */
.testimonials{position:absolute;top:1591px;left:0;width:1200px;height:401px;background:#fff}
.testimonials .sec-title{margin-top:30px}
.quote{position:relative;width:930px;margin:34px auto 0;text-align:center;font-style:italic;font-size:13.5px;line-height:26px;color:#333}
.quote .mark{font-family:"Montserrat",sans-serif;font-weight:700;font-style:normal;font-size:22px;color:#222;line-height:0}
.author{margin-top:12px;text-align:center;font-style:italic;font-weight:700;font-size:15px;color:#222}
.avatars{position:absolute;top:254px;left:444px;display:flex;gap:18px}
.avatar{width:89px;height:89px;border-radius:50%;border:4px solid #d5d5d5;background:linear-gradient(160deg,#a4a7ab,#55595f)}
.avatar.current{border-color:var(--green);position:relative}
.avatar.current::before{content:"";position:absolute;left:30px;top:-18px;border:10px solid transparent;border-bottom-color:var(--green)}

/* membership */
.membership{position:absolute;top:1992px;left:0;width:1200px;height:247px;background:var(--grey-band)}
.membership .sec-title{margin-top:26px}
.partner-box{position:absolute;left:346px;top:112px;width:506px;height:103px;background:#fff;display:flex;align-items:center;justify-content:space-around}
.partner{display:flex;align-items:center;gap:10px;font-family:"Montserrat",sans-serif;font-weight:700;font-size:30px;color:var(--partner-grey);white-space:nowrap}
.partner i{display:block;width:22px;height:22px;border-radius:50%;background:var(--partner-grey)}

/* footer */
.site-footer{position:absolute;top:2239px;left:0;width:1200px;height:284px;background:var(--footer)}
.col{position:absolute;top:38px}
.col h4{font-family:"Lato",sans-serif;font-weight:700;font-size:16px;color:#fff}
.col h4::after{content:"";display:block;width:46px;height:3px;background:var(--green);margin-top:12px}
.links{list-style:none;margin-top:18px}
.links li{font-size:13px;color:var(--footer-text);height:37px;display:flex;align-items:center}
.links li::before{content:"›";color:var(--green);font-size:17px;margin-right:10px}
.links li.on{color:#fff;font-weight:700}
.inquiry{left:345px}
.field{width:212px;height:31px;border:1px solid #e6e6e6;border-radius:3px;margin-top:8px;font-size:11px;font-weight:700;color:#ddd;padding:8px 10px}
.inquiry .field:first-of-type{margin-top:16px}
.submit{width:212px;height:34px;background:var(--green);color:#fff;font-weight:700;font-size:14px;display:flex;align-items:center;justify-content:center;margin-top:8px}
.contact{left:612px}
.contact ul{list-style:none;margin-top:18px}
.contact li{display:flex;align-items:flex-start;gap:10px;font-size:12px;color:var(--footer-text);margin-bottom:14px;line-height:16px}
.contact li strong{color:#fff}
.map{left:880px}
.map-frame{margin-top:16px;width:217px;height:153px;border:3px solid #888;background:linear-gradient(135deg,#e8eef0 0%,#a9d3ef 35%,#e3e6e0 55%,#9ccb70 100%)}

/* copyright */
.copy-bar{position:absolute;top:2523px;left:0;width:1200px;height:52px;background:var(--blue-bar);display:flex;align-items:center}
.copy-bar p{margin-left:100px;font-size:13px;color:#fff}
.social.bottom{right:100px;top:12px}
.social.bottom i{width:28px;height:28px}
</style>
</head>
<body>
<div class="wrap">

  <header class="site-header">
    <div class="brand"><span class="brand-dot"></span><span class="brand-name">Vireo Kinetics</span></div>
    <div class="brand-tag">Health And Wellness</div>
    <div class="phone-pill">
      <span class="ico"><svg width="18" height="18" viewBox="0 0 24 24"><path fill="#fff" d="M6.6 10.8a15 15 0 0 0 6.6 6.6l2.2-2.2c.3-.3.7-.4 1-.2 1.1.4 2.3.6 3.6.6.6 0 1 .4 1 1V20c0 .6-.4 1-1 1A17 17 0 0 1 3 4c0-.6.4-1 1-1h3.5c.6 0 1 .4 1 1 0 1.3.2 2.5.6 3.6.1.3 0 .7-.2 1z"/></svg></span>
      <span class="num">(555) 014 - 2290</span>
    </div>
    <div class="social top" aria-label="Social media links"><i></i><i></i><i></i></div>
    <nav class="main-nav">
      <a class="active">Home</a>
      <a>Physical Therapy</a>
      <a>Personal Training &amp; Nutritio</a>
      <a>Contact Us</a>
    </nav>
  </header>

  <section class="hero">
    <div class="hero-photo" role="img" aria-label="Athletes training with battle ropes in an indoor gym while a coach times them"></div>
    <div class="slide-arrow prev"><svg width="14" height="18" viewBox="0 0 14 18"><path d="M11 2L4 9l7 7" stroke="#fff" stroke-width="3" fill="none"/></svg></div>
    <div class="slide-arrow next"><svg width="14" height="18" viewBox="0 0 14 18"><path d="M3 2l7 7-7 7" stroke="#fff" stroke-width="3" fill="none"/></svg></div>
    <div class="hero-caption"><h2>We Educate Our Patients On How To Sustain a Healthy Lifestyle !</h2></div>
  </section>

  <section class="about">
    <h2 class="sec-title">About Vireo Kinetics <small>Health And Wellness</small></h2>
    <p class="first">We are a company that specializes in Sports Therapy,&nbsp; Physical therapy, muscular rehab, nutrition plans, and personal training. Vireo Kinetics&nbsp; travels around<br>the country and world treating athletes and people in the workforce that have Soft tissue injuries. We educate our patients on how to sustain a healthy lifestyle!</p>
    <p>We build relationships with companies committed to the sustainable health of their employees and patrons. We offer Corporate Health Solutions thro<br>ugh QMD®. Contact us today for more information About QMD®.</p>
  </section>

  <section class="specialize">
    <div class="specialize-photo" role="img" aria-label="Two athletes shaking hands in a bright gym, softly faded behind the content"></div>
    <h2 class="sec-title">We <span class="blue">Specializes In</span></h2>
    <div class="rule"></div>
    <svg class="spec-lines" width="1200" height="734" viewBox="0 0 1200 734">
      <path d="M440 258 Q560 412 440 566" stroke="#1a6fb5" stroke-width="5" fill="none" stroke-dasharray="70 12"/>
      <g stroke="#555" stroke-width="1" stroke-dasharray="3 3" fill="none">
        <path d="M462 278 L520 200 L560 200"/>
        <path d="M490 330 L525 305 L560 305"/>
        <path d="M500 411 L560 411"/>
        <path d="M490 492 L525 516 L560 516"/>
        <path d="M462 546 L520 626 L560 626"/>
      </g>
    </svg>

    <div class="spec-item" style="top:162px">
      <div class="spec-ico green"><b><svg width="30" height="30" viewBox="0 0 30 30"><path d="M15 5v20M5 15h20" stroke="#fff" stroke-width="5"/></svg></b></div>
      <div class="spec-text"><h3>SPORTS THERAPY</h3><p>Lorem ipsum dolor sit amet, consectetuer adipiscing elit, sed diam nonummy nibh euismod tincidunt ut laoreet dolore</p></div>
    </div>
    <div class="spec-item" style="top:267px">
      <div class="spec-ico blue"><b><svg width="30" height="30" viewBox="0 0 30 30"><path d="M15 26S4 19 4 11a5.5 5.5 0 0 1 11-1 5.5 5.5 0 0 1 11 1c0 8-11 15-11 15z" fill="#fff"/></svg></b></div>
      <div class="spec-text"><h3>PHYSICAL THERAPY</h3><p>Lorem ipsum dolor sit amet, consectetuer adipiscing elit, sed diam nonummy nibh euismod tincidunt ut laoreet dolore</p></div>
    </div>
    <div class="spec-item" style="top:373px">
      <div class="spec-ico blue"><b><svg width="34" height="20" viewBox="0 0 34 20"><rect x="0" y="4" width="6" height="12" fill="#fff"/><rect x="28" y="4" width="6" height="12" fill="#fff"/><rect x="6" y="8" width="22" height="4" fill="#fff"/></svg></b></div>
      <div class="spec-text"><h3>MUSCULAR REHAB</h3><p>Lorem ipsum dolor sit amet, consectetuer adipiscing elit, sed diam nonummy nibh euismod tincidunt ut laoreet dolore</p></div>
    </div>
    <div class="spec-item" style="top:478px">
      <div class="spec-ico blue"><b><svg width="24" height="30" viewBox="0 0 24 30"><rect x="2" y="4" width="20" height="24" rx="2" fill="none" stroke="#fff" stroke-width="2.5"/><path d="M6 12l2 2 3-4M6 20l2 2 3-4M14 12h5M14 20h5" stroke="#fff" stroke-width="2" fill="none"/></svg></b></div>
      <div class="spec-text"><h3>NUTRITION PLANS</h3><p>Lorem ipsum dolor sit amet, consectetuer adipiscing elit, sed diam nonummy nibh euismod tincidunt ut laoreet dolore</p></div>
    </div>
    <div class="spec-item" style="top:588px">
      <div class="spec-ico blue"><b><svg width="30" height="30" viewBox="0 0 30 30"><circle cx="15" cy="15" r="10" fill="none" stroke="#fff" stroke-width="3"/><path d="M15 9v6l4 3" stroke="#fff" stroke-width="3" fill="none"/></svg></b></div>
      <div class="spec-text"><h3>PERSONAL TRAINING</h3><p>Lorem ipsum dolor sit amet, consectetuer adipiscing elit, sed diam nonummy nibh euismod tincidunt ut laoreet dolore</p></div>
    </div>
  </section>

  <section class="testimonials">
    <h2 class="sec-title">Client <span class="blue">Testimonials</span></h2>
    <div class="rule"></div>
    <p class="quote"><span class="mark">“</span>&nbsp; Lorem ipsum dolor sit amet, consectetur adipiscing elit, sed do eiusmod tempor incididunt ut labore et dolore magna aliqua. Ut enim&nbsp; veniam, quis nostrud exercitation ullamco laboris nisi ut aliquip ex ea commodo consequat. Duis aute irure dolor in reprehenderit in voluptate velit esse cillum dolore eu fugiat nulla pariatur. Excepteur sint occaecat cupidatat non proident, sunt in culpa qui officia .&nbsp; <span class="mark">”</span></p>
    <p class="author">- Sconsectetur adipiscing</p>
    <div class="avatars">
      <div class="avatar" role="img" aria-label="Client portrait"></div>
      <div class="avatar current" role="img" aria-label="Client portrait, selected"></div>
      <div class="avatar" role="img" aria-label="Client portrait"></div>
    </div>
  </section>

  <section class="membership">
    <h2 class="sec-title">Our <span class="blue">Membership</span></h2>
    <div class="rule"></div>
    <div class="partner-box">
      <span class="partner"><i></i>QMD</span>
      <span class="partner"><i></i>Steelwave</span>
    </div>
  </section>

  <footer class="site-footer">
    <div class="col" style="left:100px">
      <h4>Quick Links</h4>
      <ul class="links">
        <li class="on">Home</li>
        <li>Physical Therapy</li>
        <li>Personal Training &amp; Nutritio</li>
        <li>Contact Us</li>
      </ul>
    </div>
    <div class="col inquiry">
      <h4>Quick Inquiry</h4>
      <div class="field">Name</div>
      <div class="field">Email</div>
      <div class="field">Message</div>
      <div class="submit">Submit</div>
    </div>
    <div class="col contact">
      <h4>Contact Details</h4>
      <ul>
        <li><svg width="12" height="16" viewBox="0 0 12 16"><path d="M6 0a6 6 0 0 1 6 6c0 4-6 10-6 10S0 10 0 6a6 6 0 0 1 6-6z" fill="#6aa22e"/><circle cx="6" cy="6" r="2" fill="#1b1b1b"/></svg><span><strong>Vireo Kinetics</strong><br>1234- Lorem ipsum dolor sitamet,<br>HARBOR CITY - USA -000000</span></li>
        <li><svg width="13" height="13" viewBox="0 0 24 24"><path fill="#6aa22e" d="M6.6 10.8a15 15 0 0 0 6.6 6.6l2.2-2.2c.3-.3.7-.4 1-.2 1.1.4 2.3.6 3.6.6.6 0 1 .4 1 1V20c0 .6-.4 1-1 1A17 17 0 0 1 3 4c0-.6.4-1 1-1h3.5c.6 0 1 .4 1 1 0 1.3.2 2.5.6 3.6.1.3 0 .7-.2 1z"/></svg><span>(555) 014 - 2290</span></li>
        <li><svg width="13" height="13" viewBox="0 0 14 14"><rect x="3" y="0" width="8" height="4" fill="#6aa22e"/><rect x="0" y="5" width="14" height="6" fill="#6aa22e"/><rect x="3" y="9" width="8" height="5" fill="#6aa22e"/></svg><span>(555) 014 - 2290</span></li>
        <li><svg width="14" height="11" viewBox="0 0 14 11"><rect width="14" height="11" fill="#6aa22e"/><path d="M0 0l7 6 7-6" stroke="#1b1b1b" stroke-width="1.5" fill="none"/></svg><span>health@vireokinetics.example</span></li>
      </ul>
    </div>
    <div class="col map">
      <h4>Location Map</h4>
      <div class="map-frame" role="img" aria-label="Street map showing the office location"></div>
    </div>
  </footer>

  <div class="copy-bar">
    <p>Copyright © 2016 Vireo Kinetics. All Rights Reserved.</p>
    <div class="social bottom" aria-label="Social media links"><i></i><i></i><i></i></div>
  </div>

</div>
</body>
</html>
```